Global Expert Network Firm needs business card design

We need business card design for a new company based in Seoul, South Korea called 'Corwell Insight Partners'. We recruit industry experts covering all countries and connect our client and recruited expert by phone, face-to-face meetings and etc. We are a global expert network firm that is focused on delivering high-quality experts to our clients throughout the world. Our clients include multinational corporations, global consulting firms, private equity firms, venture capital firms, asset management companies.
We have made new logo and please find attachment.(Please use new logo)
Target Market(s)
Global Consulting Firms, Investment Firms, Private Equity Firms, Venture Capital Firms.
Industry/Entity Type
Recruitment
Contact Information for Business Card
We need two Languages (English and Korean Version).
The front is Korean and the back is English version.
[The back] [English]
Company Name: Corwell Insight Partners, Inc.
CEO Name: Derek Hwang
Address: #508, Daerim Bldg, 72 Mokdongseo-ro, Yangcheon-gu, Seoul, 07918, Korea
Tel. +82 2 847 1215
Fax. +82 2 761 4218
Mobile. +82 10 6284 1215
Email: derek@corwellip.com
Web: www.corwellip.com
[The front] [Korean] => Described in same order as English version.
회사명: 코웰인사이트파트너스(주)
대표이사: 황도윤
주소: 서울시 양천구 목동서로 72 대림빌딩 508호
Tel. 02 847 1215
Fax. 02 761 4218
Mobile. 010 6284 1215
Web: www.corwellip.com

```html
<!DOCTYPE html>
<html lang="en">
<head>
<meta charset="utf-8">
<title>Corwell Insight Partners – Business Cards</title>
<link href="https://fonts.googleapis.com/css2?family=Noto+Sans+KR:wght@300;400;700&family=Open+Sans:wght@400;600;700&display=swap" rel="stylesheet">
<style>
  :root {
    --navy: #1b2157;
    --paper: #ffffff;
    --ink: #1f1f24;
    --muted: #55586a;
    --backdrop: #e7e6e3;
  }
  * { box-sizing: border-box; margin: 0; padding: 0; }
  html, body { width: 1200px; height: 832px; overflow: hidden; }
  body {
    background: var(--backdrop);
    display: flex; align-items: center; justify-content: center; gap: 40px;
    font-family: "Open Sans", "Noto Sans KR", sans-serif;
    color: var(--ink);
  }
  .card {
    position: relative; width: 540px; height: 309px;
    background: var(--paper);
    box-shadow: 0 6px 18px rgba(0,0,0,.15);
  }
  .brand-block {
    position: absolute; left: 0; top: 64px; width: 292px; height: 200px;
    background: var(--navy);
    display: flex; align-items: center; justify-content: center;
  }
  .brand-name {
    font-family: "Open Sans", sans-serif;
    font-weight: 400; font-size: 18px; color: #ffffff;
    white-space: nowrap;
  }
  .info {
    position: absolute; left: 318px; top: 38px; width: 196px;
  }
  .rule { height: 2px; background: var(--navy); }
  .person { margin: 14px 0 12px; }
  .person-name { font-weight: 700; font-size: 13px; line-height: 1.2; }
  .person-title { font-size: 10px; color: var(--muted); }
  .ko .person-name { font-family: "Noto Sans KR", sans-serif; font-weight: 400; font-size: 15px; }
  .ko .person-title { font-family: "Noto Sans KR", sans-serif; font-weight: 300; color: var(--muted); }
  .contacts { list-style: none; font-size: 8.6px; line-height: 1.45; margin-bottom: 14px; }
  .contact { display: flex; gap: 6px; margin-bottom: 5px; }
  .icons { display: flex; flex-direction: column; gap: 3px; width: 20px; padding-top: 2px; }
  .icons svg { width: 9px; height: 9px; fill: var(--navy); }
  .contact .lines { font-weight: 600; }
  .contact .address { font-weight: 400; }
  .ko .address { font-family: "Noto Sans KR", sans-serif; }
</style>
</head>
<body>

<article class="card en">
  <div class="brand-block">
    <div class="brand-name">Corwell Insight Partners</div>
  </div>
  <div class="info">
    <div class="rule"></div>
    <div class="person">
      <div class="person-name">Derek Hwang</div>
      <div class="person-title">CEO</div>
    </div>
    <ul class="contacts">
      <li class="contact">
        <span class="icons">
          <svg viewBox="0 0 10 10"><path d="M2 1h2l1 2-1 1c.5 1 1 1.5 2 2l1-1 2 1v2c-4 0-7-3-7-7z"/></svg>
          <svg viewBox="0 0 10 10"><rect x="2.5" y="0.5" width="5" height="9" rx="1"/></svg>
        </span>
        <span class="lines">+82 2 847 1215<br>+82 10 6284 1215</span>
      </li>
      <li class="contact">
        <span class="icons">
          <svg viewBox="0 0 10 10"><path d="M0 2h10v6H0z M0 2l5 3.5L10 2" fill="none" stroke="#1b2157" stroke-width="1"/></svg>
          <svg viewBox="0 0 10 10"><rect x="0.5" y="3" width="9" height="6"/><rect x="2.5" y="0.5" width="5" height="3"/></svg>
        </span>
        <span class="lines">derek@corwellip.com<br>+82 2 761 4218</span>
      </li>
      <li class="contact">
        <span class="icons">
          <svg viewBox="0 0 10 10"><circle cx="5" cy="5" r="4.3" fill="none" stroke="#1b2157"/><path d="M1 5h8M5 .7v8.6" stroke="#1b2157" stroke-width=".8"/></svg>
        </span>
        <span class="lines">www.corwellip.com<br><span class="address">#508, Daerim Bldg, 72 Mokdongseo-ro,<br>Yangcheon-gu, Seoul, 07918, Korea</span></span>
      </li>
    </ul>
    <div class="rule"></div>
  </div>
</article>

<article class="card ko" lang="ko">
  <div class="brand-block">
    <div class="brand-name" lang="en">Corwell Insight Partners</div>
  </div>
  <div class="info">
    <div class="rule"></div>
    <div class="person">
      <div class="person-name">황도윤</div>
      <div class="person-title">대표이사</div>
    </div>
    <ul class="contacts">
      <li class="contact">
        <span class="icons">
          <svg viewBox="0 0 10 10"><path d="M2 1h2l1 2-1 1c.5 1 1 1.5 2 2l1-1 2 1v2c-4 0-7-3-7-7z"/></svg>
          <svg viewBox="0 0 10 10"><rect x="2.5" y="0.5" width="5" height="9" rx="1"/></svg>
        </span>
        <span class="lines">+82 2 847 1215<br>+82 10 6284 1215</span>
      </li>
      <li class="contact">
        <span class="icons">
          <svg viewBox="0 0 10 10"><path d="M0 2h10v6H0z M0 2l5 3.5L10 2" fill="none" stroke="#1b2157" stroke-width="1"/></svg>
          <svg viewBox="0 0 10 10"><rect x="0.5" y="3" width="9" height="6"/><rect x="2.5" y="0.5" width="5" height="3"/></svg>
        </span>
        <span class="lines">derek@corwellip.com<br>+82 2 761 4218</span>
      </li>
      <li class="contact">
        <span class="icons">
          <svg viewBox="0 0 10 10"><circle cx="5" cy="5" r="4.3" fill="none" stroke="#1b2157"/><path d="M1 5h8M5 .7v8.6" stroke="#1b2157" stroke-width=".8"/></svg>
        </span>
        <span class="lines">www.corwellip.com<br><span class="address">서울시 양천구 목동서로 72<br>대림빌딩 508호</span></span>
      </li>
    </ul>
    <div class="rule"></div>
  </div>
</article>

</body>
</html>
```